Sale hospital laugh

With our Customer Tarvo Athletic we have the opportunity to sell our Brand Lunor Active Apparel in a Hopital. Now we need a flyer for the hopital which they can distribute to their employees. Please use font: Univers LT Std 45 Light or Univers LT Std 55 "180206_NK_Poster_A3_Staff_action.compressed" 180306_ZO_Flyer Content "As well as you find the the logos.

```html
<!DOCTYPE html>
<html lang="de">
<head>
<meta charset="utf-8">
<title>Mitarbeiteraktion – 20% Rabatt</title>
<link rel="stylesheet" href="https://fonts.googleapis.com/css2?family=Hind:wght@300;400;500&display=swap">
<style>
  :root {
    --lime: #d4e03c;
    --ink: #0b0b0b;
    --paper: #ffffff;
    --stage: #d6d6d6;
    --olive: #6d7119;
    --muted: #3a3a3a;
  }
  html, body {
    margin: 0;
    width: 1200px;
    height: 1200px;
    overflow: hidden;
    background: var(--stage);
  }
  .flyer {
    position: absolute;
    left: 180px;
    top: 10px;
    width: 840px;
    height: 1179px;
    display: block;
    font-family: "Hind", "Helvetica Neue", Arial, sans-serif;
  }
  .offer { fill: var(--lime); font-weight: 400; }
  .claim { fill: var(--ink); font-weight: 400; }
  .claim-small { fill: var(--ink); font-weight: 300; }
  .detail { fill: var(--paper); font-weight: 400; }
  .campaign { fill: var(--lime); font-weight: 400; }
  .brand { fill: var(--ink); font-weight: 500; }
  .brand-caption { fill: var(--muted); font-weight: 300; }
</style>
</head>
<body>
<svg class="flyer" viewBox="0 0 885 1242" xmlns="http://www.w3.org/2000/svg">
  <defs>
    <linearGradient id="photo-tone" x1="0" y1="0" x2="1" y2="1">
      <stop offset="0" stop-color="#e6e6e6"/>
      <stop offset="0.5" stop-color="#bdbdbd"/>
      <stop offset="1" stop-color="#9a9a9a"/>
    </linearGradient>
    <linearGradient id="highlight" x1="0" y1="0" x2="1" y2="0">
      <stop offset="0" stop-color="#0b0b0b"/>
      <stop offset="1" stop-color="#6d7119"/>
    </linearGradient>
  </defs>

  <rect class="sheet" width="885" height="1242" fill="var(--paper)"/>

  <g role="img" aria-label="Foto: Läuferin in schwarzen Kompressionsstrümpfen und weissen Laufschuhen auf einer Betontreppe">
    <polygon points="0,0 885,0 885,150 322,702 0,612" fill="url(#photo-tone)"/>
  </g>

  <!-- diagonal bands -->
  <polygon class="band" points="755,262 862,172 885,172 885,190 800,262" fill="var(--ink)"/>
  <polygon class="band" points="432,527 470,527 322,702 300,690" fill="var(--ink)"/>
  <polygon class="band-bottom" points="0,612 885,887 885,1098 0,1098" fill="var(--ink)"/>

  <!-- discount boxes -->
  <polygon points="517,380 582,262 885,262 885,380" fill="var(--ink)"/>
  <polygon points="432,527 492,402 885,402 885,527" fill="var(--ink)"/>
  <text class="offer" x="612" y="357" font-size="100">20%</text>
  <text class="offer" x="495" y="497" font-size="88">RABATT</text>

  <!-- claim badge -->
  <circle cx="676" cy="745" r="172" fill="var(--ink)"/>
  <circle cx="654" cy="750" r="172" fill="var(--lime)"/>
  <text class="claim" text-anchor="middle" font-size="38">
    <tspan x="654" y="662">Für ein</tspan>
    <tspan x="654" y="714">einzigartiges</tspan>
    <tspan x="654" y="764">Gefüh</tspan>
  </text>
  <text class="claim-small" text-anchor="middle" font-size="24">
    <tspan x="654" y="816">LUN Compressionsocks</tspan>
    <tspan x="654" y="847">und Velo-Cloud</tspan>
  </text>

  <!-- event details -->
  <rect x="162" y="774" width="232" height="52" fill="url(#highlight)"/>
  <rect x="182" y="861" width="270" height="52" fill="url(#highlight)"/>
  <rect x="182" y="940" width="130" height="48" fill="url(#highlight)"/>

  <g class="icon-calendar" fill="none" stroke="var(--lime)" stroke-width="2.5">
    <rect x="40" y="788" width="32" height="26" rx="2"/>
    <line x1="40" y1="796" x2="72" y2="796"/>
    <line x1="48" y1="783" x2="48" y2="791"/>
    <line x1="64" y1="783" x2="64" y2="791"/>
    <path d="M46 802h4M54 802h4M62 802h4M46 808h4M54 808h4M62 808h4"/>
  </g>
  <g class="icon-clock" fill="none" stroke="var(--lime)" stroke-width="3">
    <circle cx="55" cy="889" r="16"/>
    <path d="M55 879v11l7 6"/>
  </g>

  <text class="detail" x="96" y="817" font-size="42">25. April 2018</text>
  <text class="detail" x="96" y="904" font-size="42">10.00 - 14.00 Uhr</text>
  <text class="detail" x="35" y="980" font-size="40">Raum- Linde</text>

  <text class="campaign" x="442" y="1072" font-size="40" text-anchor="middle">Mitarbeiteraktion – Spital Seewald</text>

  <!-- partner names -->
  <g class="partner">
    <rect x="130" y="1146" width="12" height="12" fill="var(--ink)"/>
    <text class="brand" x="150" y="1168" font-size="34">LUN</text>
    <text class="brand-caption" x="126" y="1199" font-size="11">the smart active apparel</text>
  </g>
  <g class="partner">
    <text class="brand" x="470" y="1166" font-size="26" text-anchor="middle">Tarvo Athletic</text>
    <text class="brand-caption" x="470" y="1184" font-size="12" text-anchor="middle">Seedorf / Ost</text>
    <text class="brand-caption" x="470" y="1199" font-size="11" text-anchor="middle">tarvoathletic.ch</text>
  </g>
  <g class="partner">
    <circle cx="712" cy="1138" r="7" fill="var(--ink)"/>
    <text class="brand" x="712" y="1178" font-size="34" text-anchor="middle">Velo</text>
    <text class="brand-caption" x="712" y="1204" font-size="12" text-anchor="middle">Run on air.</text>
  </g>
</svg>
</body>
</html>
```